Quiet Harbor Hours Podcast Artwork

I need a cover for my podcast Quiet Harbor Hours that is clean, modern, and minimalist, but not too feminine

Target Market(s)

People struggling with fertility particularly women who are between the ages of 35-45 though there is a small set of listeners who are men

Requirements
Must have
• Embryo in the Zero
Should not have
• No script text

```html
<!DOCTYPE html>
<html lang="en">
<head>
<meta charset="utf-8">
<title>Quiet Harbor Hours Podcast Cover Set</title>
<link rel="stylesheet" href="https://fonts.googleapis.com/css2?family=Didact+Gothic&family=Tenor+Sans&display=swap">
<style>
  :root {
    --stage-green: #8cc63f;
    --ink: #41363f;
    --ink-soft: #5a4e58;
    --sage: #9aaa82;
    --paper: #ffffff;
    --paper-shade: #ececec;
    --cover-shadow: rgba(40, 60, 10, 0.35);
  }
  html, body {
    margin: 0;
    padding: 0;
    overflow: hidden;
  }
  .stage {
    position: relative;
    width: 1200px;
    height: 545px;
    background: var(--stage-green);
    overflow: hidden;
  }
  .cover {
    position: absolute;
    display: block;
    box-shadow: 0 10px 10px -6px var(--cover-shadow);
  }
  .cover--main { left: 51px; top: 64px; width: 417px; height: 417px; }
  .cover--thumb { width: 199px; height: 199px; }
  .col-1 { left: 504px; }
  .col-2 { left: 721px; }
  .col-3 { left: 941px; }
  .row-1 { top: 64px; }
  .row-2 { top: 282px; }
  .cover-title {
    font-family: "Didact Gothic", sans-serif;
    fill: var(--ink);
  }
  .cover-label {
    font-family: "Tenor Sans", sans-serif;
    fill: var(--sage);
    letter-spacing: 0.12em;
  }
  .ink { fill: var(--ink); }
  .artwork-slot { fill: url(#artwork-tone); }
</style>
</head>
<body>
<main class="stage">
  <svg width="0" height="0" style="position:absolute" aria-hidden="true">
    <defs>
      <linearGradient id="paper-fade" x1="0" y1="0" x2="1" y2="1">
        <stop offset="0" stop-color="var(--paper)"/>
        <stop offset="0.5" stop-color="#f6f6f6"/>
        <stop offset="1" stop-color="var(--paper-shade)"/>
      </linearGradient>
      <radialGradient id="artwork-tone" cx="0.5" cy="0.45" r="0.6">
        <stop offset="0" stop-color="var(--ink)"/>
        <stop offset="1" stop-color="var(--ink-soft)"/>
      </radialGradient>
      <symbol id="thumb-cover" viewBox="0 0 249 249">
        <rect width="249" height="249" fill="url(#paper-fade)"/>
        <path class="ink" d="M0 0H85L70 20 55 40 40 52 20 60 0 66Z"/>
        <path class="ink" d="M249 162L228 172 214 186 200 205 190 230 182 249H249Z"/>
        <rect class="artwork-slot" x="95" y="55" width="75" height="80" rx="14" role="img" aria-label="Illustration area: profile head silhouette in ink with embryo motif"/>
        <text class="cover-title" x="124.5" y="173" font-size="23.5" text-anchor="middle">Quiet Harbor Hours</text>
        <text class="cover-label" x="124.5" y="190" font-size="11.5" text-anchor="middle">PODCAST</text>
      </symbol>
    </defs>
  </svg>

  <svg class="cover cover--main" viewBox="0 0 521 521" aria-label="Quiet Harbor Hours podcast cover">
    <rect width="521" height="521" fill="url(#paper-fade)"/>
    <path class="ink" d="M0 0H235L215 30 190 70 160 105 120 140 80 165 40 178 0 185Z"/>
    <path class="ink" d="M521 345L495 358 470 375 450 400 432 440 418 480 408 521H521Z"/>
    <rect class="artwork-slot" x="226" y="115" width="130" height="165" rx="24" role="img" aria-label="Illustration area: profile head silhouette in ink with embryo motif"/>
    <text class="cover-title" x="260.5" y="350" font-size="44" text-anchor="middle">Quiet Harbor Hours</text>
    <text class="cover-label" x="260.5" y="388" font-size="25" text-anchor="middle">PODCAST</text>
  </svg>

  <svg class="cover cover--thumb col-1 row-1" aria-label="Quiet Harbor Hours podcast cover"><use href="#thumb-cover"/></svg>
  <svg class="cover cover--thumb col-2 row-1" aria-label="Quiet Harbor Hours podcast cover"><use href="#thumb-cover"/></svg>
  <svg class="cover cover--thumb col-3 row-1" aria-label="Quiet Harbor Hours podcast cover"><use href="#thumb-cover"/></svg>
  <svg class="cover cover--thumb col-1 row-2" aria-label="Quiet Harbor Hours podcast cover"><use href="#thumb-cover"/></svg>
  <svg class="cover cover--thumb col-2 row-2" aria-label="Quiet Harbor Hours podcast cover"><use href="#thumb-cover"/></svg>
  <svg class="cover cover--thumb col-3 row-2" aria-label="Quiet Harbor Hours podcast cover"><use href="#thumb-cover"/></svg>
</main>
</body>
</html>
```